New Office Poster Designs

Attached you will find 3 poster designs that we found online along with our logos. Please use our logos to reference any type of color or design.
These posters will be hung around our Loan Offices.

INSTRUCTIONS: Please mimic all 3 posters (MINUS THE SMALL WRITING ON THEM THAT IS NOT IN ENGLISH IGNORE THAT)
but use our logos and colors. Also, if you can make them in Spanish as well as English that is a plus. We will also need 1 additional poster with the below wording.

Additional Poster:
Stuck in a Title Loan? Let us pay it off up to $10,000

Target Market(s)

People looking to get a loan and need money

Industry/Entity Type

Loan Industry - Consumer Lending - Fast easy loans

Requirements
Nice to have
• English and Spanish

```html
<!DOCTYPE html>
<html lang="en">
<head>
<meta charset="utf-8">
<title>Title Loan Payoff Poster</title>
<link href="https://fonts.googleapis.com/css2?family=Bebas+Neue&family=Roboto+Condensed:wght@400&display=swap" rel="stylesheet">
<style>
  :root {
    --page-bg: #ebebeb;
    --poster-red: #e4252b;
    --poster-red-light: #ec3a3f;
    --text-white: #ffffff;
    --divider: rgba(255, 255, 255, 0.45);
    --brand-green: #1f5a36;
    --brand-red: #d0202a;
  }
  html, body {
    margin: 0;
    padding: 0;
    width: 1200px;
    height: 1200px;
    overflow: hidden;
    background: var(--page-bg);
  }
  .poster {
    position: absolute;
    left: 206px;
    top: 90px;
    width: 788px;
    height: 1020px;
    overflow: hidden;
    font-family: "Bebas Neue", "Arial Narrow", sans-serif;
    color: var(--text-white);
    text-align: center;
  }
  .money-backdrop {
    position: absolute;
    inset: 0;
    background: radial-gradient(ellipse at 50% 40%, var(--poster-red-light), var(--poster-red) 70%);
  }
  .headline {
    position: absolute;
    left: 0;
    right: 0;
    margin: 0;
    font-weight: 400;
    line-height: 1;
  }
  .headline-top { top: 92px; font-size: 108px; }
  .headline-bottom { top: 218px; font-size: 108px; }
  .divider {
    position: absolute;
    left: 244px;
    width: 350px;
    top: 345px;
    height: 1px;
    background: var(--divider);
  }
  .offer {
    position: absolute;
    left: 0;
    right: 0;
    margin: 0;
    line-height: 1;
    font-weight: 400;
  }
  .offer-lead { top: 406px; font-size: 54px; }
  .offer-upto { top: 474px; font-size: 74px; }
  .offer-amount { top: 548px; font-size: 152px; letter-spacing: 2px; }
  .brand-arch {
    position: absolute;
    left: 219px;
    width: 352px;
    top: 710px;
    bottom: 0;
    background: var(--text-white);
    border-radius: 176px 176px 0 0 / 130px 130px 0 0;
  }
  .brand-name {
    position: absolute;
    left: 0;
    right: 0;
    top: 132px;
    margin: 0;
    font-size: 56px;
    line-height: 1;
    font-weight: 400;
    color: var(--brand-green);
  }
  .brand-url {
    position: absolute;
    left: 0;
    right: 0;
    top: 200px;
    margin: 0;
    font-family: "Roboto Condensed", "Arial Narrow", sans-serif;
    font-size: 18px;
    color: var(--brand-red);
  }
</style>
</head>
<body>
  <main class="poster">
    <div class="money-backdrop" role="img" aria-label="Red-tinted background of scattered hundred-dollar bills"></div>
    <h1 class="headline headline-top">Stuck in a</h1>
    <h1 class="headline headline-bottom">Title Loan?</h1>
    <div class="divider"></div>
    <p class="offer offer-lead">Let us pay it off</p>
    <p class="offer offer-upto">Up to</p>
    <p class="offer offer-amount">$10,000</p>
    <div class="brand-arch">
      <p class="brand-name">Crestline Loans</p>
      <p class="brand-url">www.crestlineloans.com</p>
    </div>
  </main>
</body>
</html>
```